8.5 x 8.5 - HELOC Product Campaign

Home Equity Lines of Credit
are BACK!!!

* Up to 97.5% on Owner Occupied Properties
* 700 Minimum Scores
* Fund in only 2-3 weeks

Can be used for...
* Education Expense
* Bill Consolidation
* Home Improvement
* Investments

Call today for more information!
(800) 417-2960

Bluegate Lending Partners, Inc.
NMLS #381760
www.bluegatelendhub.com

```html
<!DOCTYPE html>
<html lang="en">
<head>
<meta charset="utf-8">
<title>Bluegate Lending Partners – HELOC Campaign</title>
<link rel="stylesheet" href="https://fonts.googleapis.com/css2?family=Montserrat:wght@400;500;600;700;800&display=swap">
<style>
  :root{
    --brand-blue:#0b5ca9;
    --navy:#173f6e;
    --phone-blue:#1d4f86;
    --gold:#b39a3b;
    --white:#ffffff;
    --rule:#2a2a2a;
  }
  *{margin:0;padding:0;box-sizing:border-box}
  html,body{width:1200px;height:1200px;overflow:hidden;background:#fff}
  body{font-family:'Montserrat',sans-serif;color:var(--navy)}
  .ad{position:relative;width:1200px;height:1200px;overflow:hidden;background:var(--white)}
  .ad-shapes{position:absolute;inset:0}
  .headline{
    position:absolute;left:232px;top:212px;width:520px;
    transform:translate(-50%,-50%) rotate(-45deg);
    color:var(--white);text-align:center;font-size:50px;font-weight:500;line-height:1.02;letter-spacing:1px;
  }
  .headline strong{font-weight:800;display:block;font-size:54px}
  .features{position:absolute;left:84px;top:577px;width:390px;list-style:none}
  .feature{display:flex;align-items:center;gap:22px;font-weight:700;font-size:24px;line-height:1.25;color:var(--navy)}
  .feature + .feature{border-top:1px solid var(--rule)}
  .feature:nth-child(1){height:82px;padding-bottom:8px}
  .feature:nth-child(2){height:61px}
  .feature:nth-child(3){height:61px}
  .feature .hl{color:var(--gold)}
  .feature svg{flex:none;width:38px;height:38px}
  .cta{
    position:absolute;left:83px;top:804px;width:472px;height:36px;border-radius:18px;
    background:var(--navy);color:var(--white);font-size:20px;font-weight:500;
    display:flex;align-items:center;justify-content:center;letter-spacing:.3px;
  }
  .phone-icon{position:absolute;left:80px;top:864px;width:72px;height:76px}
  .phone{position:absolute;left:164px;top:850px;font-size:52px;font-weight:500;line-height:1.1;color:var(--phone-blue);letter-spacing:1px;white-space:nowrap}
  .web{position:absolute;left:196px;top:914px;font-size:22px;font-weight:700;color:var(--gold);white-space:nowrap}
  .brand{position:absolute;left:66px;top:1050px;width:290px;display:flex;align-items:center;gap:14px;font-size:20px;font-weight:700;line-height:1.25;color:var(--navy)}
  .brand-dot{flex:none;width:30px;height:30px;border-radius:50%;background:var(--gold)}
  .company{position:absolute;left:390px;top:1070px;font-size:13px;color:#1c1c1c;line-height:1.3}
  .company-name{font-size:18px;font-weight:700;color:var(--navy);margin-bottom:8px}
  .company-line{display:flex;gap:8px;align-items:flex-start;margin-bottom:6px}
  .company-line svg{flex:none;margin-top:2px}
  .uses{
    position:absolute;left:826px;top:1045px;width:340px;
    transform-origin:0 0;transform:rotate(-45deg);
    color:var(--white);white-space:nowrap;
  }
  .uses-lead{font-size:20px;line-height:24px;font-weight:500;letter-spacing:.5px}
  .uses ul{list-style:none;font-size:29px;font-weight:500;line-height:36px}
  .uses li::before{content:"•";margin-right:14px}
  .eho-badge{position:absolute;left:1092px;top:1092px;width:74px;height:74px;border:3px solid var(--white);border-radius:4px}
</style>
</head>
<body>
<main class="ad">
  <svg class="ad-shapes" width="1200" height="1200" viewBox="0 0 1200 1200">
    <defs>
      <linearGradient id="photoSofa" x1="0" y1="0" x2="1" y2="1">
        <stop offset="0" stop-color="#eae6e1"/><stop offset=".55" stop-color="#c7b4a2"/><stop offset="1" stop-color="#9a7250"/>
      </linearGradient>
      <linearGradient id="photoGrad" x1="0" y1="0" x2="0" y2="1">
        <stop offset="0" stop-color="#b6a58c"/><stop offset="1" stop-color="#1f2a3e"/>
      </linearGradient>
      <linearGradient id="photoPlan" x1="0" y1="0" x2="1" y2="1">
        <stop offset="0" stop-color="#d9d6db"/><stop offset="1" stop-color="#9b95ad"/>
      </linearGradient>
      <linearGradient id="photoPaint" x1="0" y1="0" x2="1" y2="1">
        <stop offset="0" stop-color="#eceae8"/><stop offset="1" stop-color="#6d6a7e"/>
      </linearGradient>
    </defs>
    <path class="corner-band" d="M0 0H630L18 612Q0 630 0 606Z" fill="var(--brand-blue)"/>
    <polygon role="img" aria-label="Photo: couple on a sofa looking at a tablet" points="634,0 1200,0 1200,607 1030,768 448,186" fill="url(#photoSofa)"/>
    <path role="img" aria-label="Photo: smiling graduate in cap and gown" d="M450 211L630 394L453 574L295 410Q282 397 295 384Z" fill="url(#photoGrad)"/>
    <polygon role="img" aria-label="Photo: couple reviewing home plans" points="637,399 820,585 648,772 519,640 519,520" fill="url(#photoPlan)"/>
    <path role="img" aria-label="Photo: couple painting a room" d="M836 600L1015 780L850 938Q836 952 822 938L656 776Z" fill="url(#photoPaint)"/>
    <path class="uses-band" d="M1200 645V1200H828L755 1118Q744 1105 756 1093Z" fill="var(--brand-blue)"/>
  </svg>

  <h1 class="headline">HOME<br>EQUITY LINES<br>OF CREDIT ARE<strong>BACK!!!</strong></h1>

  <ul class="features">
    <li class="feature">
      <svg viewBox="0 0 40 40" fill="none" stroke="var(--gold)" stroke-width="2.2"><path d="M9 19L20 9L31 19M12 17V27H28V17"/><rect x="17" y="19" width="6" height="5"/><path d="M3 30Q12 26 20 31L34 27"/></svg>
      <span>Up to <span class="hl">97.5%</span> on Owner Occupied Properties</span>
    </li>
    <li class="feature">
      <svg viewBox="0 0 40 40" fill="none" stroke="var(--gold)" stroke-width="2"><rect x="8" y="6" width="24" height="30" rx="2"/><rect x="15" y="3" width="10" height="6" rx="1"/><path d="M12 15h4M12 22h4M12 29h4M19 15h9M19 22h9M19 29h6"/></svg>
      <span><span class="hl">700</span> Minimum Scores</span>
    </li>
    <li class="feature">
      <svg viewBox="0 0 40 40" fill="none" stroke="var(--gold)" stroke-width="2.2"><rect x="5" y="8" width="30" height="27" rx="2"/><path d="M5 15H35M13 4V11M27 4V11M5 22H35M5 28H35M15 15V35M25 15V35"/></svg>
      <span>Fund in only <span class="hl">2-3</span> weeks</span>
    </li>
  </ul>

  <p class="cta">CALL TODAY FOR MORE INFORMATION!</p>

  <svg class="phone-icon" viewBox="0 0 72 76"><rect x="20" y="2" width="42" height="72" rx="6" fill="none" stroke="var(--phone-blue)" stroke-width="6"/><path d="M0 42Q0 30 12 28L24 26V70L10 68Q0 66 0 56Z" fill="var(--phone-blue)"/><rect x="54" y="38" width="16" height="7" rx="3" fill="var(--phone-blue)"/><rect x="54" y="48" width="16" height="7" rx="3" fill="var(--phone-blue)"/><rect x="54" y="58" width="14" height="7" rx="3" fill="var(--phone-blue)"/></svg>
  <p class="phone">(800) 417-2960</p>
  <p class="web">www.bluegatelendhub.com</p>

  <div class="brand"><span class="brand-dot"></span><span>Bluegate Lending<br>Partners, Inc.</span></div>

  <div class="company">
    <p class="company-name">Bluegate Lending Partners, Inc.</p>
    <p class="company-line"><svg width="10" height="13" viewBox="0 0 10 13"><path d="M5 12C2 8 1 6 1 4.5A4 4 0 0 1 9 4.5C9 6 8 8 5 12Z" fill="none" stroke="var(--gold)" stroke-width="1.4"/></svg><span>MARYLAND OFFICE: 740 Alder Creek Rd,<br>Columbia, MD 21044</span></p>
    <p class="company-line"><svg width="10" height="13" viewBox="0 0 10 13"><rect x="1" y="3" width="5" height="5" fill="var(--gold)"/></svg><span>NMLS #381760</span></p>
  </div>

  <div class="uses">
    <p class="uses-lead">CAN BE USED FOR...</p>
    <ul>
      <li>Education Expense</li>
      <li>Bill Consolidation</li>
      <li>Home Improvement</li>
      <li>Investments</li>
    </ul>
  </div>

  <div class="eho-badge" aria-hidden="true"></div>
</main>
</body>
</html>
```